Environmental Plastics Infographic on Marine Debris

We need a series of infographics that can be used individually or as a combined presentation. We'd like the combined piece to include an introduction and conclusion along with 4-5 infographics. Each infographic (information unit) should also work as a standalone. We are trying to help people visualize size proportions and ratios to put the plastics marine debris problem in perspective. Our key point is concerning polystyrene foam which represents 35 tons. We are looking for something creative to help people understand what the problem represents in terms they are familiar with.

To view our typical company design/style please see our website at www.harbenfoamworks.org. Our primary RGB colors are: (187,140,9); (94,47,29); (94,138,164); and (164,167,15). Secondary RGB colors are (249,162,28) and (218,210,208). Our title/header font is DIN Next LT Pro and our copy font is Calibri 10.5 pt. We can deviate from the font specification if beneficial and welcome interesting text treatments and typography.

Need extra days to review

Target Market(s)

international brand manufacturers (brenloch, tavix), US legislators & government agencies

Font styles to use
Sans Serif

Requirements
Must have
• Sufficient white space. Easy to grasp message concept with visual components.

```html
<!DOCTYPE html>
<html lang="en">
<head>
<meta charset="utf-8">
<title>Plastics Weight Comparison</title>
<link rel="stylesheet" href="https://fonts.googleapis.com/css2?family=Open+Sans:wght@400;700&display=swap">
<style>
  :root {
    --orange: #f7a31e;
    --hex-grey: #dad3d2;
    --card: #f3eeee;
    --navy: #0d2a38;
    --connector: #f3eeee;
  }
  html, body {
    margin: 0;
    padding: 0;
    overflow: hidden;
  }
  body {
    width: 1200px;
    height: 899px;
    background: var(--orange);
    font-family: "Open Sans", sans-serif;
    color: var(--navy);
  }
  .infographic {
    position: relative;
    width: 1200px;
    height: 899px;
  }
  .diagram {
    position: absolute;
    inset: 0;
  }
  .stat-card {
    position: absolute;
    width: 259px;
    height: 192px;
    background: var(--card);
    box-sizing: border-box;
    padding-top: 28px;
    text-align: center;
  }
  .stat-card.two-line { padding-top: 8px; }
  .stat-label {
    font-size: 25px;
    line-height: 32px;
    letter-spacing: 0.3px;
  }
  .stat-sublabel {
    font-size: 19px;
    line-height: 28px;
  }
  .stat-value {
    margin-top: 6px;
    font-size: 38px;
    font-weight: 700;
    line-height: 52px;
  }
  .stat-unit {
    font-size: 37px;
    line-height: 52px;
  }
  .card-gpgp   { left: 74px;  top: 70px; }
  .card-ship   { left: 869px; top: 70px; }
  .card-nyc    { left: 74px;  top: 638px; }
  .card-whale  { left: 869px; top: 638px; }
  .weight-text { font-family: "Open Sans", sans-serif; fill: var(--hex-grey); text-anchor: middle; }
</style>
</head>
<body>
<main class="infographic">
  <svg class="diagram" width="1200" height="899" viewBox="0 0 1200 899">
    <defs>
      <symbol id="weight" viewBox="0 0 100 160">
        <path fill="#0d2a38" fill-rule="evenodd"
          d="M50,0 C78,0 100,15 100,40 C100,55 92,62 88,66 L12,66 C8,62 0,55 0,40 C0,15 22,0 50,0 Z
             M50,18 C34,18 22,26 22,38 C22,46 26,52 30,56 L70,56 C74,52 78,46 78,38 C78,26 66,18 50,18 Z"/>
        <path fill="#0d2a38"
          d="M8,70 Q8,58 20,56 L80,56 Q92,58 92,70 L98,148 Q98,156 90,156 Q50,162 10,156 Q2,156 2,148 Z"/>
        <text class="weight-text" x="50" y="112" font-size="46">50</text>
        <text class="weight-text" x="50" y="138" font-size="22">TONS</text>
      </symbol>
    </defs>

    <!-- connectors -->
    <g class="connectors" stroke="var(--connector)" stroke-width="6">
      <line x1="333" y1="166" x2="610" y2="166"/>
      <line x1="998" y1="262" x2="998" y2="400"/>
      <line x1="203" y1="498" x2="203" y2="638"/>
      <line x1="586" y1="733" x2="869" y2="733"/>
    </g>

    <!-- hexagons -->
    <g class="hexagons" fill="var(--hex-grey)">
      <polygon points="425,286 512,134 690,134 776,286 690,438 512,438"/>
      <polygon points="152,444 240,292 416,292 504,444 416,596 240,596"/>
      <polygon points="698,444 786,291 962,291 1050,444 962,596 786,596"/>
      <polygon points="425,604 512,452 690,452 776,604 690,756 512,756"/>
    </g>

    <!-- GPGP plastics: 1.5 weights -->
    <g class="weights-gpgp">
      <use href="#weight" x="528" y="222" width="82" height="128"/>
      <svg x="632" y="222" width="41" height="128" viewBox="0 0 52 160" preserveAspectRatio="xMinYMin slice">
        <use href="#weight" x="0" y="0" width="100" height="160"/>
      </svg>
    </g>

    <!-- NYC weekly waste -->
    <g class="weights-nyc">
      <use href="#weight" x="254" y="353" width="54" height="85"/>
      <use href="#weight" x="348" y="353" width="54" height="85"/>
      <use href="#weight" x="254" y="450" width="54" height="85"/>
      <use href="#weight" x="348" y="450" width="54" height="85"/>
      <svg x="320" y="402" width="15" height="85" viewBox="0 0 28 160" preserveAspectRatio="xMinYMin slice">
        <use href="#weight" x="0" y="0" width="100" height="160"/>
      </svg>
    </g>

    <!-- Cruise ship -->
    <g class="weights-ship">
      <use href="#weight" x="788" y="386" width="75" height="117"/>
      <use href="#weight" x="886" y="386" width="75" height="117"/>
    </g>

    <!-- Blue whale -->
    <g class="weights-whale">
      <use href="#weight" x="538" y="513" width="54" height="85"/>
      <use href="#weight" x="610" y="513" width="54" height="85"/>
      <use href="#weight" x="538" y="610" width="54" height="85"/>
      <use href="#weight" x="610" y="610" width="54" height="85"/>
    </g>
  </svg>

  <section class="stat-card card-gpgp">
    <div class="stat-label">All GPGP Plastics</div>
    <div class="stat-value">78,908</div>
    <div class="stat-unit">TONS</div>
  </section>

  <section class="stat-card card-ship">
    <div class="stat-label">One Cruise Ship</div>
    <div class="stat-value">100,000</div>
    <div class="stat-unit">TONS</div>
  </section>

  <section class="stat-card card-nyc two-line">
    <div class="stat-label">One Week</div>
    <div class="stat-sublabel">NYC Waste Generation</div>
    <div class="stat-value">269,230</div>
    <div class="stat-unit">TONS</div>
  </section>

  <section class="stat-card card-whale">
    <div class="stat-label">One Blue Whale</div>
    <div class="stat-value">200,000</div>
    <div class="stat-unit">TONS</div>
  </section>
</main>
</body>
</html>
```